Kelp Webcomic

A simple signup landing page and blog design for an upcoming webcomic. I am mostly looking for a flat UI with a simple color scheme. I want to showcase a large background image and the comic title image. I have all the technicals figured out (I am a web developer by trade), so all I need now is a solid design I like.

The signup for should only have one field (email) and have text above it, and smaller text below it.

The blog, I am thinking, should be in the style of comic book pages. The home page would be blocks with large white outlines, with the article pages being an extension of that. As I stated before, should be fairly minimalist, but fun. Also, no sidebar or ads, IE single column. I have attached a simple mockup/layout of the blog to give a general idea of what I am going for.

I have attached the Logo and Background art (uncolored) for reference. Don't worry about the background image blending in, I can take care of that when the design is implemented. I will be focusing on layout and overall look, not necessarily readability (which I can fix).

~Please DO NOT take these examples literally. I will describe what I like about each example.~

Signup pages:
http://example-plinth.com/landing-page-type-photo/
http://www.example-varnoq.com/showcase/website-design/814/10-most-beautiful-landing-pages-in-minimalist-style
http://example-quellbay.com/47-modern-landing-pages-showcasing-inspirational-web-design/
Great examples of minimalist design. However, instead of text or other content, there should be a simple signup form, as described above. Also think a lot more "playful" rather than super professional.

Blog:
http://example-vradd.no/
Awesome example of a single column, minimal design. Needs to be more "comicbook style" though.
http://example-tumbrik.com/
Another good example of minimal design blog.
http://example-morvane.net/wp-content/uploads/res-blogs-5.jpg
I like the timeline feel here. Combine that with a comic book page kind of thing, and I think you have a winner.

Actual webcomic landing (not required):
http://www.example-fennowhistle.com/comic.php?date=20021104#.U90ysYBdUvU
I like the navigation. It makes the atmosphere nice for the comic. The page layout itself is WAY too busy.
http://www.example-lodgeworth.com/comic/
Fairly common webcomic, but their navigation and page layout is nice.
http://example-qwib.com/936/
Another common webcomic. The simple page layout makes it easy for people to get started I think.

So there you have it. I will try my best to keep updating and adding to the description. If you have any questions, please don't hesitate to ask.

Hey Guys, I am really appreciating all the effort you have been putting in. I am amazed to see all the awesome designs and all the care taken with the project. I am just writing everyone to let you know that I have uploaded a simple layout/wireframe of the blog, to give an idea of what I am going for. Can't wait to see how things progress, and good luck to everyone!

Industry/Entity Type

Trade

Font styles to use
Sans Serif

Requirements
Must have
• Must showcase a large background image (does not have to cover the entire background). Should be a flat UI as well. Should be mostly neutral with splashes of blue or purple. Social links should also be somewhere (twitter, facebook, etc.).
Nice to have
• I am thinking something with rounded boxes, but I can live without them. A more "fun" design as opposed to more professional is definitely nice to have.

If you would like to try a stab at the actual comic page display and navigation, you are welcome to submit something. It should not be a main priority though.

Being responsive is not a requirement, but it would be nice to have.
Should not have
• A billion links in the navigation or look too busy.
No sidebar or advertisements. Should be a clean design.

```html
<!DOCTYPE html>
<html lang="en">
<head>
<meta charset="utf-8">
<title>Kelp Webcomic</title>
<link rel="stylesheet" href="https://fonts.googleapis.com/css2?family=Open+Sans:wght@400;600&family=Exo:wght@300&family=Bebas+Neue&display=swap">
<style>
  :root {
    --accent: #7b6ff6;
    --accent-dark: #5d52d6;
    --ink: #1d1d1f;
    --paper: #ffffff;
    --btn-dark: #444446;
    --header-top: #c6d4dc;
    --header-bottom: #dfe3e6;
    --footer-a: #7fd6c4;
    --footer-b: #9fd6cc;
    --footer-c: #4fc6b2;
    --icon-bg: #bfeee2;
    --social: #5b6fa8;
    --platform: #9fc23c;
  }
  * { box-sizing: border-box; margin: 0; padding: 0; }
  html, body { width: 1200px; height: 868px; overflow: hidden; }
  body { font-family: "Open Sans", Arial, sans-serif; color: var(--ink); background: #8fa7a6; }

  .page { position: relative; width: 1200px; height: 868px; overflow: hidden; }

  .top-strip { position: absolute; left: 0; top: 0; width: 1200px; height: 6px; background: var(--accent); }

  .site-header {
    position: absolute; left: 0; top: 6px; width: 1200px; height: 108px;
    background: linear-gradient(180deg, var(--header-top), var(--header-bottom));
    box-shadow: 0 2px 4px rgba(0,0,0,.25); z-index: 2;
  }
  .brand {
    position: absolute; left: 100px; top: 30px;
    font-family: "Open Sans", Arial, sans-serif; font-weight: 600; font-size: 44px;
    line-height: 48px; color: #2c2a3a; letter-spacing: 1px;
    display: flex; align-items: center; gap: 12px;
  }
  .brand-dot { width: 18px; height: 18px; border-radius: 50%; background: var(--accent); }

  .main-nav { position: absolute; top: 33px; right: 92px; display: flex; align-items: center; }
  .main-nav a {
    font-size: 13px; color: var(--ink); text-decoration: none;
    padding: 0 17px; line-height: 40px; border-radius: 7px;
  }
  .main-nav a.active { background: var(--accent); color: var(--paper); padding: 0 27px; }

  .hero {
    position: absolute; left: 0; top: 114px; width: 1200px; height: 616px;
    background:
      radial-gradient(ellipse 260px 220px at 120px 120px, rgba(140,70,70,.75), transparent 70%),
      radial-gradient(ellipse 300px 200px at 520px 60px, rgba(60,60,60,.7), transparent 70%),
      radial-gradient(ellipse 340px 260px at 900px 280px, rgba(200,215,205,.7), transparent 70%),
      radial-gradient(ellipse 300px 220px at 1120px 360px, rgba(70,80,75,.7), transparent 70%),
      radial-gradient(ellipse 400px 200px at 200px 460px, rgba(60,130,110,.6), transparent 70%),
      linear-gradient(180deg, #8f9f98 0%, #7fa39c 45%, #3fa79a 100%);
  }

  .phone {
    position: absolute; left: 108px; top: 68px; width: 236px; height: 500px;
    border-radius: 36px; background: #0c0c0e; border: 3px solid #2a2a2e;
    box-shadow: 0 6px 8px rgba(0,0,0,.3); overflow: hidden;
  }
  .phone-screen {
    position: absolute; left: 16px; top: 70px; width: 202px; height: 356px;
    background: linear-gradient(160deg, #f2f2f2, #9a9a9a 50%, #d8d8d8);
  }
  .phone-home {
    position: absolute; left: 95px; bottom: 14px; width: 44px; height: 44px;
    border-radius: 50%; background: #1b1b1e; border: 1px solid #333;
  }
  .phone-home::after {
    content: ""; position: absolute; left: 14px; top: 14px; width: 14px; height: 14px;
    border: 2px solid #888; border-radius: 3px;
  }
  .ribbon {
    position: absolute; left: -42px; top: 52px; width: 330px; height: 42px;
    background: var(--accent); color: var(--paper); transform: rotate(-31deg);
    font-family: "Exo", Arial, sans-serif; font-weight: 300; font-size: 24px;
    line-height: 42px; text-align: center;
  }

  .hero-copy { position: absolute; left: 375px; top: 102px; width: 700px; color: var(--paper); }
  .hero-title { font-family: "Exo", Arial, sans-serif; font-weight: 300; font-size: 30px; line-height: 36px; margin-bottom: 8px; }
  .hero-copy p { font-size: 14px; line-height: 24px; margin: 0 0 9px 3px; width: 690px; }
  .hero-copy p.justified { text-align: justify; }

  .actions { position: absolute; left: 380px; top: 323px; display: flex; gap: 12px; }
  .btn {
    width: 120px; height: 43px; border-radius: 7px; color: var(--paper);
    font-size: 15px; line-height: 43px; text-align: center;
  }
  .btn-login { background: var(--btn-dark); }
  .btn-signup { background: var(--accent); }

  .newsletter { position: absolute; left: 379px; top: 384px; }
  .newsletter h2 { font-weight: 400; font-size: 25px; color: var(--paper); line-height: 34px; margin-bottom: 8px; }
  .signup-row { display: flex; gap: 15px; }
  .email-field {
    width: 536px; height: 49px; background: var(--paper); font-size: 14px;
    line-height: 49px; padding-left: 15px; color: #222;
  }
  .submit {
    width: 170px; height: 49px; background: var(--accent); color: var(--paper);
    font-family: "Bebas Neue", Arial, sans-serif; font-size: 26px; letter-spacing: 1px;
    line-height: 51px; text-align: center;
  }

  .store-row { position: absolute; left: 379px; top: 502px; display: flex; align-items: center; gap: 12px; }
  .store-badge { height: 62px; border-radius: 5px; background: #050505; border: 1px solid #333; }
  .store-badge.one { width: 184px; }
  .store-badge.two { width: 194px; }
  .platform-mark { width: 46px; height: 52px; margin-left: 28px; border-radius: 10px; background: var(--platform); }

  .site-footer {
    position: absolute; left: 0; top: 730px; width: 1200px; height: 138px;
    background:
      radial-gradient(ellipse 300px 120px at 700px 40px, rgba(190,220,215,.6), transparent 70%),
      linear-gradient(90deg, var(--footer-c), var(--footer-a) 40%, var(--footer-b) 70%, var(--footer-a));
    border-top: 1px solid rgba(255,255,255,.3);
  }
  .quick-links { position: absolute; left: 96px; top: 30px; display: flex; }
  .quick-link { display: flex; flex-direction: column; align-items: center; font-size: 15px; color: #1f2a2a; }
  .quick-link .icon {
    width: 44px; height: 44px; border-radius: 50%; background: var(--icon-bg);
    box-shadow: 0 2px 3px rgba(0,0,0,.2); display: flex; align-items: center; justify-content: center;
    margin-bottom: 6px;
  }
  .quick-link .icon svg { width: 26px; height: 26px; fill: none; stroke: var(--accent); stroke-width: 2.6; stroke-linecap: round; stroke-linejoin: round; }
  .ql-search { width: 56px; }
  .ql-links { width: 56px; margin-left: 22px; }
  .ql-settings { width: 56px; margin-left: 26px; }
  .ql-reports { width: 60px; margin-left: 30px; }
  .ql-signup { width: 60px; margin-left: 28px; }

  .social { position: absolute; left: 917px; top: 40px; display: flex; gap: 18px; }
  .social span { width: 32px; height: 32px; background: var(--social); display: block; }
  .copyright { position: absolute; right: 101px; top: 83px; font-size: 14px; color: #1f2a2a; }
</style>
</head>
<body>
<div class="page">
  <div class="top-strip"></div>

  <header class="site-header">
    <div class="brand"><span>Kelp</span><span class="brand-dot"></span></div>
    <nav class="main-nav">
      <a class="active" href="#">Home</a>
      <a href="#">About Us</a>
      <a href="#">Serives</a>
      <a href="#">Blog</a>
      <a href="#">Testimonials</a>
      <a href="#">Contact Us</a>
    </nav>
  </header>

  <section class="hero" role="img" aria-label="Large blurred background artwork in muted red, grey and teal tones">
    <div class="phone">
      <div class="phone-screen" role="img" aria-label="Black and white comic page artwork shown on the phone screen"></div>
      <div class="ribbon">Coming Soon</div>
      <div class="phone-home"></div>
    </div>

    <div class="hero-copy">
      <h1 class="hero-title">We create the most Kelp</h1>
      <p>Lorem ipsum dolor sit amet, consectetuer adipiscing elit. Aenean commodo ligula eget dolor. Aenean massa. Cum sociis natoque penatibus et magnis dis parturient montes, nascetur ridiculus mus.</p>
      <p class="justified">Rrem ipsum dolor sit amet, consectetuer adipiscing elit. Aenean commodo ligula eget dolor. Aenean massa. Cum sociis natoque penatibus et magnis dis parturient montes, nascetur ridiculus mus. Cum sociis natoque penatibus et magnis dis parturient montes, nascetur ridiculus mus. Donec quam felis, ultricies nec, pellentesque eu, pretium quis, sem. Nulla consequat massa quis enim.</p>
    </div>

    <div class="actions">
      <div class="btn btn-login">Login</div>
      <div class="btn btn-signup">Sign Up</div>
    </div>

    <div class="newsletter">
      <h2>Newsletters</h2>
      <div class="signup-row">
        <div class="email-field">Email Address</div>
        <div class="submit">Submit</div>
      </div>
    </div>

    <div class="store-row">
      <div class="store-badge one" role="img" aria-label="First app store download badge"></div>
      <div class="store-badge two" role="img" aria-label="Second app store download badge"></div>
      <div class="platform-mark" role="img" aria-label="Mobile platform mark"></div>
    </div>
  </section>

  <footer class="site-footer">
    <div class="quick-links">
      <div class="quick-link ql-search">
        <div class="icon"><svg viewBox="0 0 26 26"><circle cx="10" cy="10" r="6.5"/><line x1="15" y1="15" x2="22" y2="22"/></svg></div>
        Search
      </div>
      <div class="quick-link ql-links">
        <div class="icon"><svg viewBox="0 0 26 26"><circle cx="9" cy="9" r="5"/><circle cx="17" cy="17" r="5"/><line x1="11" y1="11" x2="15" y2="15"/></svg></div>
        Links
      </div>
      <div class="quick-link ql-settings">
        <div class="icon"><svg viewBox="0 0 26 26"><circle cx="13" cy="13" r="6"/><circle cx="13" cy="13" r="2"/><path d="M13 3v4M13 19v4M3 13h4M19 13h4M6 6l3 3M17 17l3 3M20 6l-3 3M6 20l3-3"/></svg></div>
        Settings
      </div>
      <div class="quick-link ql-reports">
        <div class="icon"><svg viewBox="0 0 26 26"><rect x="5" y="4" width="16" height="18" rx="1.5"/><line x1="9" y1="18" x2="9" y2="14"/><line x1="13" y1="18" x2="13" y2="10"/><line x1="17" y1="18" x2="17" y2="12"/></svg></div>
        Reports
      </div>
      <div class="quick-link ql-signup">
        <div class="icon"><svg viewBox="0 0 26 26"><path d="M13 5H6v16h7"/><line x1="10" y1="13" x2="22" y2="13"/><path d="M18 9l4 4-4 4"/></svg></div>
        Sign Up
      </div>
    </div>

    <div class="social" aria-label="Social links">
      <span></span><span></span><span></span><span></span>
    </div>
    <div class="copyright">Copyright © Kelp 2014. All rights reserved.</div>
  </footer>
</div>
</body>
</html>
```